The Tarnvale Classic for Midfield Legends™

Please go to www.tarnvaleclassic.example and if you are a professional web designer you know what needs to be done!
I need a fresh, modern but still 'credible' design (authority!) - after all the event is an official World Championship!
Content (text, pics etc.) remains the same.
A new, trademarked logo has been developed and needs to be used throughout the site.
The site must include the possibility to be able to update/change content by ourselfs using a simple CMS.
Project duration: 5 days or less.
Main reason being for such a short period of time: we are AT PRESENT in negociations with all kinds of stakeholders and would like to impress them ASAP!
Could be an ongoing job for next couple of months.
Key words: official World Championship, golf, football, first sports cross over event ever, authority, fun, BRAZIL (hosting country), excitement, television, country's honour, another Ardent Shield, PASSION!!
Pictures on website can be used - our/my responsibility.
Good luck!

Target Market(s)

(ex) Footballers - european soccer.
Golfers
People interested in sports

Industry/Entity Type

Event

Requirements
Must have
• Golf
Football
Brazil
Authority
World Championship

```html
<!DOCTYPE html>
<html lang="en">
<head>
<meta charset="utf-8">
<title>The Tarnvale Classic for Midfield Legends™</title>
<link href="https://fonts.googleapis.com/css2?family=Open+Sans:ital,wght@0,400;0,600;0,700;0,800;1,800&display=swap" rel="stylesheet">
<style>
:root{
  --topbar:#3b3b3b;
  --nav-top:#f4f4f4;
  --nav-bottom:#e2e2e2;
  --accent:#f0a21a;
  --button-top:#ffd23a;
  --button-bottom:#f3a713;
  --ink:#3a3a3a;
  --muted:#555;
  --rule:#cfcfcf;
  --panel:#ffffff;
  --page-top:#fbfbfb;
  --page-bottom:#e6e6e6;
  --footer-top:#3a3a3a;
  --footer-bottom:#6a6a6a;
  --footer-text:#e8e8e8;
  --gold:#b9964b;
}
*{margin:0;padding:0;box-sizing:border-box}
html,body{width:934px;height:1200px;overflow:hidden}
body{position:relative;font-family:Arial,Helvetica,sans-serif;color:var(--ink);
  background:linear-gradient(var(--page-top) 300px,var(--page-bottom) 1000px)}
.abs{position:absolute}
.heading{font-family:"Open Sans",sans-serif;font-weight:400;color:var(--ink)}

/* top bar and navigation */
.topbar{left:0;top:0;width:934px;height:30px;background:var(--topbar);color:#fff;
  font-family:"Open Sans",sans-serif;font-size:9.5px}
.topbar .contact{top:9px;display:flex;align-items:center;gap:5px}
.navbar{left:0;top:30px;width:934px;height:40px;background:linear-gradient(var(--nav-top),var(--nav-bottom));
  border-bottom:1px solid #cfcfcf}
.nav{right:195px;top:44px;display:flex;align-items:center;font-family:"Open Sans",sans-serif;font-size:9.5px;color:#444;z-index:2}
.nav span{padding:0 0 0 16px}
.nav .sep{color:#777;font-size:8px}
.nav .current{color:var(--accent);text-decoration:underline;padding-left:0}
.brand{left:198px;top:4px;width:148px;height:92px;background:#fff;border-radius:10px 10px 22px 22px;
  box-shadow:0 1px 3px rgba(0,0,0,.25);z-index:3;display:flex;flex-direction:column;align-items:center;justify-content:center;gap:6px;text-align:center}
.brand .dot{width:30px;height:30px;border-radius:50%;background:var(--gold)}
.brand .name{font-family:"Open Sans",sans-serif;font-weight:600;font-size:7.5px;line-height:10px;color:var(--gold);padding:0 10px}

/* hero */
.hero{left:0;top:70px;width:934px;height:230px;
  background:linear-gradient(100deg,#3f8a2a 0%,#5aa43a 45%,#6fae4a 60%,#9fb7a0 75%,#d8dcd6 88%,#7da35c 100%)}
.hero-title{left:204px;top:134px;font-family:"Open Sans",sans-serif;font-style:italic;font-weight:800;font-size:29px;color:#fff;letter-spacing:-.3px}
.hero-sub{left:203px;top:167px;font-family:"Open Sans",sans-serif;font-weight:600;font-size:10px;color:#fff}
.hero-note{left:205px;top:184px;font-size:6.5px;color:#fff}
.button{left:205px;top:204px;width:106px;height:21px;border-radius:2px;
  background:linear-gradient(var(--button-top),var(--button-bottom));border:1px solid #d38e0c;
  font-weight:700;font-size:9.5px;color:#1d1d1d;display:flex;align-items:center;justify-content:center}

/* main panel */
.panel{left:194px;top:272px;width:545px;height:720px;border-radius:6px 6px 0 0;
  background:linear-gradient(#fff 0,#fff 300px,rgba(255,255,255,0) 700px)}
.intro-title{left:210px;top:285px;font-size:14px}
.intro-date{left:210px;top:308px;font-family:"Open Sans",sans-serif;font-size:8px;text-decoration:underline;color:#333}
.intro-text{left:210px;top:331px;width:345px;font-size:6.5px;line-height:12px;color:var(--muted)}
.intro-text p+p{margin-top:12px}

.side-title{left:567px;font-size:14px}
.calendar{left:568px;top:311px;width:160px;height:130px;border:1px solid var(--rule);background:#fff;padding:8px 10px 0 10px}
.calendar .month{font-family:"Open Sans",sans-serif;font-size:15px;color:#444;display:flex;justify-content:space-between;letter-spacing:.8px}
.calendar .grid{margin-top:10px;display:grid;grid-template-columns:repeat(7,1fr);row-gap:1px;
  font-family:"Open Sans",sans-serif;font-size:9px;line-height:12px;color:#444}
.calendar .grid b{font-weight:700}

.candidates-title{left:210px;top:452px;font-size:14px}
.candidates{left:210px;top:480px;width:341px;height:253px;border:1px solid var(--rule);border-radius:2px;background:#fafafa}
.photo{width:70px;height:86px;border:1px solid #ccc}
.caption{width:90px;text-align:center;font-size:7.5px;font-style:italic;color:#444}
.caption b{font-weight:700}

.news{left:568px;width:160px;display:flex;gap:7px}
.news .avatar{width:27px;height:27px;flex:none;border:1px solid #bbb;background:linear-gradient(#d9c2b2,#8b6f60)}
.news p{font-size:7px;line-height:11px;color:#444}

/* marketing carousel */
.marketing-title{left:210px;top:753px;font-size:14px}
.bubble{width:84px;height:84px;border-radius:50%;border:3px solid #fff;box-shadow:0 1px 3px rgba(0,0,0,.35)}
.bubble-label{width:100px;text-align:center;font-size:8.5px;line-height:11px;color:#444}
.dots{left:451px;top:914px;display:flex;gap:3px}
.dots i{width:9px;height:9px;border-radius:50%;background:#444;display:block}
.dots i.on{background:#fff;border:2px solid #444}
.points{left:203px;top:950px;font-size:8.5px;color:#333;list-style:none}
.points li{line-height:17.5px}
.points li::before{content:"•";margin-right:9px}

/* footer */
.footer{left:0;top:1004px;width:934px;height:196px;background:radial-gradient(ellipse at 50% 130%,var(--footer-bottom),var(--footer-top) 75%)}
.footer-col{top:1017px;width:162px}
.footer-col h3{font-family:"Open Sans",sans-serif;font-weight:400;font-size:17px;color:#fff;padding-bottom:3px;border-bottom:1px solid #777;white-space:nowrap}
.footer-address{font-family:"Open Sans",sans-serif;font-size:8px;line-height:11px;color:var(--footer-text);margin-top:11px;padding-left:2px}
.footer-address p+p{margin-top:9px}
.flags{margin-top:11px;display:grid;grid-template-columns:repeat(5,24px);column-gap:5.5px;row-gap:5.5px}
.flags svg{width:24px;height:24px;display:block}
.social{margin-top:11px;display:flex;gap:8px}
.social span{display:flex;align-items:center;gap:4px;font-family:"Open Sans",sans-serif;font-size:8px;color:#fff}
.social i{width:14px;height:14px;border-radius:50%;background:#fff;display:block}
</style>
</head>
<body>

<header>
  <div class="abs topbar">
    <div class="abs contact" style="left:523px">
      <svg width="6" height="9" viewBox="0 0 6 9"><rect x="0.5" y="0.5" width="5" height="8" rx="1" fill="none" stroke="#fff"/><rect x="2" y="7" width="2" height="1" fill="#fff"/></svg>
      <span>+ 34 600 418 352</span>
    </div>
    <div class="abs contact" style="left:623px">
      <svg width="9" height="7" viewBox="0 0 9 7"><rect width="9" height="7" fill="#fff"/><path d="M0 0L4.5 4L9 0" fill="none" stroke="#3b3b3b"/></svg>
      <span>office@tarnvaleops.example</span>
    </div>
  </div>
  <div class="abs navbar"></div>
  <div class="abs brand">
    <span class="dot"></span>
    <span class="name">The Tarnvale Classic for Midfield Legends™</span>
  </div>
  <nav class="abs nav">
    <span class="current">Home</span><span class="sep">I</span>
    <span>Event</span><span class="sep">I</span>
    <span>Ambassadors</span><span class="sep">I</span>
    <span>TVC/Contact</span>
  </nav>
</header>

<section>
  <div class="abs hero" role="img" aria-label="Football resting in the goal net on a grass pitch"></div>
  <h1 class="abs hero-title">THE BEST FREE WAY</h1>
  <p class="abs hero-sub">THE TARNVALE CLASSIC FOR MIDFIELD LEGENDS.</p>
  <p class="abs hero-note">Lorem Ipsum is simply dummy text of the printing and typesetting industry.</p>
  <div class="abs button">LEARN MORE</div>
</section>

<main>
  <div class="abs panel"></div>

  <h2 class="abs heading intro-title">The Tarnvale Classic for Midfield Legends™</h2>
  <p class="abs intro-date">June 5-8, 2014, Rio de Janeiro, Brazil</p>
  <div class="abs intro-text">
    <p>One doesn't need to be a fanatical supporter of either golf or football to get a sense of just how much interest and excitement the Tarnvale Classic for Midfield Legends™ will generate: an A-list of current and former players and coaches from the world's most popular spectator sport, playing the world's fastest growing participation sport, on the world's most beautiful golf courses, just has to be a winner!</p>
    <p>"These guys have performed in front of millions of people on a weekly basis. It will be fascinating to see how they hold their nerves outside their comfort zones but still in a very competitive environment..."</p>
  </div>

  <h2 class="abs heading side-title" style="top:285px">Events Calendar</h2>
  <div class="abs calendar">
    <div class="month"><span>NOVEMBER</span><span>2013</span></div>
    <div class="grid">
      <b>S</b><b>M</b><b>T</b><b>W</b><b>T</b><b>F</b><b>S</b>
      <span></span><span></span><span>1</span><span>2</span><span>3</span><span>4</span><span>5</span>
      <span>6</span><span>7</span><span>8</span><span>9</span><span>10</span><span>11</span><span>12</span>
      <span>13</span><span>14</span><span>15</span><span>16</span><span>17</span><span>18</span><span>19</span>
      <span>20</span><span>21</span><span>22</span><span>23</span><span>24</span><span>25</span><span>26</span>
      <span>27</span><span>28</span><span>29</span><span>30</span>
    </div>
  </div>

  <h2 class="abs heading candidates-title">Potential Candidates</h2>
  <div class="abs candidates"></div>
  <div class="abs photo" style="left:225px;top:493px;background:linear-gradient(#9bb27e,#5f8d4a)" role="img" aria-label="Golfer in green shirt on the course"></div>
  <div class="abs photo" style="left:305px;top:493px;background:linear-gradient(#e9d27a,#c9433c)" role="img" aria-label="Golfer in red shirt lining up a putt"></div>
  <div class="abs photo" style="left:386px;top:493px;background:linear-gradient(#6f8f5a,#a7b49a)" role="img" aria-label="Golfer mid swing among trees"></div>
  <div class="abs photo" style="left:467px;top:493px;background:linear-gradient(#8a8f92,#1e2a33)" role="img" aria-label="Player portrait in dark shirt"></div>
  <p class="abs caption" style="left:214px;top:590px"><b>Varga</b> (Germany)</p>
  <p class="abs caption" style="left:294px;top:590px"><b>Moreau</b> (Protugal)</p>
  <p class="abs caption" style="left:375px;top:590px"><b>Halloran</b> (Spain)</p>
  <p class="abs caption" style="left:456px;top:590px"><b>Van Esch</b> (Holland)</p>
  <div class="abs photo" style="left:225px;top:613px;background:linear-gradient(#223322,#2f7fb0)" role="img" aria-label="Golfer in blue shirt finishing a swing"></div>
  <div class="abs photo" style="left:305px;top:613px;background:linear-gradient(#7f9a76,#2e3f5a)" role="img" aria-label="Golfer following a drive"></div>
  <div class="abs photo" style="left:386px;top:613px;background:linear-gradient(#4d7a3a,#1f2a20)" role="img" aria-label="Golfer in black swinging on the fairway"></div>
  <div class="abs photo" style="left:467px;top:613px;background:linear-gradient(#7c8a7a,#3a2f2f)" role="img" aria-label="Golfer in red and black at the top of a swing"></div>
  <p class="abs caption" style="left:214px;top:709px"><b>Varga</b> (Germany)</p>
  <p class="abs caption" style="left:294px;top:709px"><b>Moreau</b> (Protugal)</p>
  <p class="abs caption" style="left:375px;top:709px"><b>Halloran</b> (Spain)</p>
  <p class="abs caption" style="left:456px;top:709px"><b>Van Esch</b> (Holland)</p>

  <h2 class="abs heading side-title" style="top:452px">Latest News</h2>
  <div class="abs news" style="top:486px"><span class="avatar" role="img" aria-label="News author portrait"></span><p>Lorem Ipsum is simply dummy text of the printing and typesetting industry.</p></div>
  <div class="abs news" style="top:530px"><span class="avatar" role="img" aria-label="News author portrait"></span><p>Lorem Ipsum is simply dummy text of the printing and typesetting industry.</p></div>
  <div class="abs news" style="top:575px"><span class="avatar" role="img" aria-label="News author portrait"></span><p>Lorem Ipsum is simply dummy text of the printing and typesetting industry.</p></div>
  <div class="abs news" style="top:619px"><span class="avatar" role="img" aria-label="News author portrait"></span><p>Lorem Ipsum is simply dummy text of the printing and typesetting industry.</p></div>
  <div class="abs news" style="top:664px"><span class="avatar" role="img" aria-label="News author portrait"></span><p>Lorem Ipsum is simply dummy text of the printing and typesetting industry.</p></div>
  <div class="abs news" style="top:708px"><span class="avatar" role="img" aria-label="News author portrait"></span><p>Lorem Ipsum is simply dummy text of the printing and typesetting industry.</p></div>

  <h2 class="abs heading marketing-title">TVC Marketing</h2>
  <svg class="abs" style="left:193px;top:816px" width="20" height="38" viewBox="0 0 20 38"><path d="M19 1L2 19L19 37" fill="none" stroke="#555" stroke-width="1.5"/></svg>
  <svg class="abs" style="left:722px;top:816px" width="20" height="38" viewBox="0 0 20 38"><path d="M1 1L18 19L1 37" fill="none" stroke="#555" stroke-width="1.5"/></svg>
  <div class="abs bubble" style="left:222px;top:793px;background:radial-gradient(#d9a56e,#3c6b3a)" role="img" aria-label="Cheering fans in festival costume"></div>
  <div class="abs bubble" style="left:323px;top:793px;background:radial-gradient(circle at 50% 60%,#1c2a1a,#4f8a34)" role="img" aria-label="Golf driver beside a ball on the tee"></div>
  <div class="abs bubble" style="left:425px;top:793px;background:radial-gradient(#ffffff 0,#ffffff 18%,#2d8a2d 30%,#1d6a1d)" role="img" aria-label="Football in the back of the net"></div>
  <div class="abs bubble" style="left:526px;top:793px;background:linear-gradient(#6f7f9a,#7fae5a 55%,#111 75%)" role="img" aria-label="Fan raising arms in a stadium"></div>
  <div class="abs bubble" style="left:628px;top:793px;background:radial-gradient(#5c5c5c,#2c2c2c 60%,#8fa878)" role="img" aria-label="Camera operator filming a match"></div>
  <p class="abs bubble-label" style="left:214px;top:882px">Official Ardent Shield<br>Championship</p>
  <p class="abs bubble-label" style="left:315px;top:888px">Golf</p>
  <p class="abs bubble-label" style="left:417px;top:888px">Football</p>
  <p class="abs bubble-label" style="left:518px;top:888px">Excitement</p>
  <p class="abs bubble-label" style="left:620px;top:888px">Television</p>
  <div class="abs dots"><i></i><i class="on"></i><i></i></div>

  <ul class="abs points">
    <li>Championship is not about money but about countries honour.....!!'</li>
    <li>Event appeals to a huge audience:&nbsp; 80 million golfers and 300 million footballers world wide.'</li>
  </ul>
</main>

<footer>
  <div class="abs footer"></div>
  <div class="abs footer-col" style="left:193px">
    <h3>The Tarnvale Classic</h3>
    <div class="footer-address">
      <p>TVC - Marketing Lda<br>Rua das Palmas 12<br>9000 - 118 Porto Moniz<br>Madeira - Portugal<br>Tel. Lena Vormark,<br>Managing Partner: + 34 600 418 352<br>Mail: office@tarnvaleops.example</p>
      <p>© TVC Marketing Lda. All rights reserved</p>
    </div>
  </div>
  <div class="abs footer-col" style="left:384px">
    <h3>Participating Trams</h3>
    <div class="flags">
      <svg viewBox="0 0 24 24"><clipPath id="c"><circle cx="12" cy="12" r="12"/></clipPath><g clip-path="url(#c)"><rect width="24" height="24" fill="#c60b1e"/><rect y="6" width="24" height="12" fill="#ffc400"/></g></svg>
      <svg viewBox="0 0 24 24"><g clip-path="url(#c)"><rect width="8" height="24" fill="#009246"/><rect x="8" width="8" height="24" fill="#fff"/><rect x="16" width="8" height="24" fill="#ce2b37"/></g></svg>
      <svg viewBox="0 0 24 24"><g clip-path="url(#c)"><rect width="24" height="8" fill="#000"/><rect y="8" width="24" height="8" fill="#dd0000"/><rect y="16" width="24" height="8" fill="#ffce00"/></g></svg>
      <svg viewBox="0 0 24 24"><g clip-path="url(#c)"><rect width="24" height="24" fill="#009c3b"/><path d="M12 4L22 12L12 20L2 12Z" fill="#ffdf00"/><circle cx="12" cy="12" r="4.5" fill="#002776"/></g></svg>
      <svg viewBox="0 0 24 24"><g clip-path="url(#c)"><rect width="24" height="24" fill="#fff"/><rect width="24" height="3" fill="#b22234"/><rect y="6" width="24" height="3" fill="#b22234"/><rect y="12" width="24" height="3" fill="#b22234"/><rect y="18" width="24" height="3" fill="#b22234"/><rect width="11" height="12" fill="#3c3b6e"/></g></svg>
      <svg viewBox="0 0 24 24"><g clip-path="url(#c)"><rect width="24" height="24" fill="#012169"/><path d="M0 0L24 24M24 0L0 24" stroke="#fff" stroke-width="4"/><path d="M12 0V24M0 12H24" stroke="#fff" stroke-width="6"/><path d="M12 0V24M0 12H24" stroke="#c8102e" stroke-width="3"/></g></svg>
      <svg viewBox="0 0 24 24"><g clip-path="url(#c)"><rect width="24" height="24" fill="#c8102e"/><path d="M9 0V24M0 12H24" stroke="#fff" stroke-width="3"/></g></svg>
      <svg viewBox="0 0 24 24"><g clip-path="url(#c)"><rect width="24" height="8" fill="#fff"/><rect y="8" width="24" height="8" fill="#0039a6"/><rect y="16" width="24" height="8" fill="#d52b1e"/></g></svg>
      <svg viewBox="0 0 24 24"><g clip-path="url(#c)"><rect width="24" height="24" fill="#74acdf"/><rect y="8" width="24" height="8" fill="#fff"/><circle cx="12" cy="12" r="2" fill="#f6b40e"/></g></svg>
      <svg viewBox="0 0 24 24"><g clip-path="url(#c)"><rect width="24" height="8" fill="#ae1c28"/><rect y="8" width="24" height="8" fill="#fff"/><rect y="16" width="24" height="8" fill="#21468b"/></g></svg>
      <svg viewBox="0 0 24 24"><g clip-path="url(#c)"><rect width="24" height="24" fill="#ff0000"/><rect width="10" height="24" fill="#006600"/><circle cx="10" cy="12" r="4" fill="#ffcc00"/></g></svg>
      <svg viewBox="0 0 24 24"><g clip-path="url(#c)"><rect width="24" height="24" fill="#fff"/><circle cx="12" cy="12" r="5" fill="#cd2e3a"/><path d="M7 12A5 5 0 0 0 17 12Z" fill="#0047a0"/></g></svg>
      <svg viewBox="0 0 24 24"><g clip-path="url(#c)"><rect width="8" height="24" fill="#0055a4"/><rect x="8" width="8" height="24" fill="#fff"/><rect x="16" width="8" height="24" fill="#ef4135"/></g></svg>
      <svg viewBox="0 0 24 24"><g clip-path="url(#c)"><rect width="8" height="24" fill="#169b62"/><rect x="8" width="8" height="24" fill="#fff"/><rect x="16" width="8" height="24" fill="#ff883e"/></g></svg>
      <svg viewBox="0 0 24 24"><g clip-path="url(#c)"><rect width="24" height="24" fill="#0d5eaf"/><rect y="5" width="24" height="2.7" fill="#fff"/><rect y="10.5" width="24" height="2.7" fill="#fff"/><rect y="16" width="24" height="2.7" fill="#fff"/><rect width="10" height="10" fill="#0d5eaf"/><path d="M5 0V10M0 5H10" stroke="#fff" stroke-width="2"/></g></svg>
      <svg viewBox="0 0 24 24"><g clip-path="url(#c)"><rect width="8" height="24" fill="#000"/><rect x="8" width="8" height="24" fill="#fdda24"/><rect x="16" width="8" height="24" fill="#ef3340"/></g></svg>
    </div>
  </div>
  <div class="abs footer-col" style="left:577px">
    <h3>Follow us</h3>
    <div class="social">
      <span><i></i>Circlo</span>
      <span><i></i>Chirpa</span>
      <span><i></i>Frendo</span>
    </div>
  </div>
</footer>

</body>
</html>
```